Career Launch DL brochure

I need a design for a double sided card and 6 page flyer to hand out to students to promote our Corvane Career Launch Program. It is an 8 week program that gives budding Accountants exposure to real-life case studies in Bookkeeping & Accounting. The design for the business cards we give students at completion of the program is done. I would like some DL cards and a 6 page brochure to match the business card design. I want a template so I can just add the text I need. I have attached a sample 6 page brochure I use for employers and the business cards we use for students (2 different markets). Make sure your design matches the look of the business cards.
Updates

Reason: So far I only have one designer and I need a few more. I would prefer to work with a designer who has looked at the business card that I uploaded and come up with a design which incorporates the colours, the look and feel. Once this is agreed, the DL brochure can be done quickly I would imagine. The DL card will have very little text and will be more about design with a short message, It will be used as a Mail Out to send out in the mail to capture interest in the program.

I have extended the deadline by 24 hours due to the lack of responses. If you intend making a submission but cannot meet the deadline, please let me know at mirethd@corvanebk.com.au I am looking for a good design which matches our business card (uploaded in the brief), please do not just put all the photos at the top of every page and leave the text in a boring font with little thought to the layout. I am looking for something different. That is why I have not gone to a printer who will just dump my text straight into someone elses template. If I find a designer with a bit of spark, I am happy to guide you through until it is right. Due to the time restrictions now, I will close the applications once I find the right designer. I don't want 10 designers, I only want 1 or 2 good ones and I happy to pay a fee for second prize, or work with them exclusively on another project. The colours are already there, this should be a fairly straight forward job. I think also, the business cards are very bold, the brochure should be less bold but still be obvious that it follows the same design.

Target Market(s)

Accounting Graduates currently studying and those employed but working in non-financial jobs. Looking for work experience so they can get their foot in the door.

Industry/Entity Type

Business

Requirements
Must have
• Matching design to the attached business cards. Must be creative. Include both DL and brochure layout.
Should not have
• The attached brochure is a sample of our Employer brochure, this should be different to the student brochure in this new design.

```html
<!DOCTYPE html>
<html lang="en">
<head>
<meta charset="utf-8">
<title>Corvane Career Launch – DL Brochure</title>
<link rel="stylesheet" href="https://fonts.googleapis.com/css2?family=Lato:wght@400;700;900&display=swap">
<style>
  :root {
    --navy: #0c4a79;
    --navy-deep: #083a61;
    --green: #7fc241;
    --white: #ffffff;
    --paper: #f6f7f8;
    --ink: #3b3f44;
    --stage: #e4e4e4;
    --link: #1b4f8a;
  }
  * { box-sizing: border-box; margin: 0; padding: 0; }
  html, body { width: 1200px; height: 982px; overflow: hidden; }
  body {
    background: var(--stage);
    font-family: "Lato", Arial, sans-serif;
    color: var(--ink);
  }
  .brochure {
    position: absolute;
    left: 48px; top: 101px;
    width: 1104px; height: 780px;
    display: flex;
    box-shadow: 0 6px 24px rgba(0,0,0,0.18);
  }
  .panel { position: relative; width: 368px; height: 780px; overflow: hidden; }

  /* Inside panel */
  .panel--info { background: linear-gradient(180deg, var(--white), var(--paper)); }
  .section-tab {
    display: block;
    width: 330px;
    margin-top: 40px;
    padding: 10px 16px 10px 22px;
    background: var(--green);
    color: var(--white);
    font-weight: 700;
    font-size: 12.5px;
    border-radius: 0 22px 22px 0;
    letter-spacing: 0.2px;
  }
  .section-tab + .section-body { margin-top: 14px; }
  .section-body {
    padding: 0 26px 0 24px;
    font-size: 11.5px;
    line-height: 1.55;
    color: #555a60;
  }
  .section-tab--second { margin-top: 120px; }
  .brand {
    display: flex; align-items: center; gap: 10px;
    font-weight: 900; color: var(--link);
  }
  .brand__mark { width: 34px; height: 34px; background: var(--green); flex: none; }
  .brand__name { font-size: 26px; line-height: 1.05; }
  .panel--info .brand { position: absolute; left: 26px; bottom: 150px; }

  /* Cover-back panel */
  .panel--contact { background: var(--navy); color: var(--white); }
  .panel--contact .brand {
    position: absolute; left: 0; right: 0; top: 230px;
    justify-content: center; color: var(--white);
  }
  .panel--contact .brand__mark { background: var(--white); }
  .contact {
    position: absolute; right: 34px; top: 470px;
    text-align: right; font-size: 13px; line-height: 1.7;
    font-style: normal;
  }
  .contact strong { font-weight: 700; }
  .web-band {
    position: absolute; left: 0; right: 0; bottom: 46px;
    height: 50px; background: var(--green);
    display: flex; align-items: center; justify-content: center;
    font-weight: 700; font-size: 18px; color: var(--white);
  }

  /* Cover panel */
  .panel--cover { background: linear-gradient(180deg, var(--white), var(--paper)); }
  .cover-photo {
    position: absolute; left: 0; top: 0; width: 368px; height: 340px;
    background: linear-gradient(160deg, #d9d3cc 0%, #b9a89a 45%, #5b6f8a 100%);
  }
  .cover-swoosh { position: absolute; left: 0; top: 300px; width: 368px; height: 140px; }
  .presenter-photo {
    position: absolute; left: 0; top: 335px; width: 104px; height: 445px;
    background: linear-gradient(180deg, #c9b6a6 0%, #2d3440 30%, #1d222b 100%);
    border-radius: 48px 48px 0 0;
  }
  .headline {
    position: absolute; left: 116px; right: 20px; top: 452px;
    text-align: right; font-weight: 900; font-size: 24px; line-height: 1.1;
    color: var(--navy);
  }
  .headline__accent { color: var(--green); }
  .panel--cover .brand { position: absolute; right: 22px; top: 600px; }
  .panel--cover .brand__name { font-size: 24px; }
  .cover-web {
    position: absolute; left: 116px; right: 20px; bottom: 50px;
    text-align: right;
    font-weight: 700; font-size: 12.5px; color: var(--link);
  }
</style>
</head>
<body>
<main class="brochure">

  <section class="panel panel--info">
    <h2 class="section-tab">VIVAMUS MASSA MASSA, TEMPOR ET LEO EGET</h2>
    <p class="section-body">Etiam ultrices sodales tellus, et imperdiet lorem viverra sit amet. Morbi convallis vitae nunc et tempus. Quisque accumsan metus nunc, iaculis blandit arcu suscipit nec. Sed rutrum libero non molestie consectetur. Pellentesque facilisis, tellus et dapibus ultrices, enim metus rutrum magna, ac convallis eros mi interdum velit. Nam faucibus leo ac rhoncus posuere.</p>
    <h2 class="section-tab section-tab--second">VIVAMUS MASSA MASSA, TEMPOR ET LEO EGET</h2>
    <p class="section-body">Etiam ultrices sodales tellus, et imperdiet lorem viverra sit amet. Morbi convallis vitae nunc et tempus. Quisque accumsan metus nunc, iaculis blandit arcu suscipit nec. Sed rutrum libero non molestie consectetur.</p>
    <div class="brand">
      <span class="brand__mark"></span>
      <span class="brand__name">Corvane<br>Career Launch</span>
    </div>
  </section>

  <section class="panel panel--contact">
    <div class="brand">
      <span class="brand__mark"></span>
      <span class="brand__name">Corvane<br>Career Launch</span>
    </div>
    <address class="contact">
      <strong>Address:</strong><br>
      Suite 4 / 12 Harlow Street, Kelvin NSW 2150<br>
      <strong>Ph:</strong> +61 2 5550 4182<br>
      <strong>Fx:</strong> +61 2 5550 4190<br>
      <strong>Email:</strong> info@CorvaneCareerLaunch.com.au
    </address>
    <div class="web-band">www.CorvaneCareerLaunch.com.au</div>
  </section>

  <section class="panel panel--cover">
    <div class="cover-photo" role="img" aria-label="Photo of a group of smiling students holding folders in a bright hallway"></div>
    <svg class="cover-swoosh" viewBox="0 0 368 140" aria-hidden="true">
      <path d="M0 55 Q190 -5 368 30 L368 62 Q190 30 0 85 Z" fill="var(--green)"/>
      <path d="M0 78 Q190 25 368 55 L368 110 Q200 70 0 130 Z" fill="var(--navy)"/>
      <path d="M0 124 Q200 64 368 104 L368 140 L0 140 Z" fill="var(--white)"/>
    </svg>
    <div class="presenter-photo" role="img" aria-label="Photo of a young man in a suit pointing towards the headline"></div>
    <h1 class="headline">LOREM IPSUM<br>DOLOR SIT AMET<br><span class="headline__accent">CONSECTETUR</span><br>ADIPISCING ELIT.</h1>
    <div class="brand">
      <span class="brand__mark"></span>
      <span class="brand__name">Corvane<br>Career Launch</span>
    </div>
    <p class="cover-web">www.CorvaneCareerLaunch.com.au</p>
  </section>

</main>
</body>
</html>
```